Quiet Harbor Counseling Business Card design with a visually interesting use of Space

I need business cards that are luxurious and give a peaceful, calm vibe. I also had some letterhead designed, and i like the look of it also, it's attached with the logo design for reference/ ideas but feel free to be creative.

Target Market(s)

High end luxurious client who needs counseling

Industry/Entity Type

Marriage and Family Therapy

Contact Information for Business Card

Corra Mabbitt MS LMFT/ or Tobin Walsh address 4175 Pemberly Suite 620

Font styles to use
Sans Serif

Colors
0054AA
0677BA
7BADD7
CADEEF
E8F1F8
0094D4
00A9DD
6FCCEA
C7EBF8
E9F6FB
A7469A
B969AE
D3A5CF
EDDBEB
F8F0F9
6B429C
8869AF
B7A5CE
E3DAEB
F3F0F8

Requirements
Must have
• Logo and color scheme but be simple modern and luxurious
Nice to have
• I'd like to incorporate some elelmets from the logo and letterhead into a simple modern card

```html
<!DOCTYPE html>
<html lang="en">
<head>
<meta charset="utf-8">
<title>Quiet Harbor Counseling – Business Card</title>
<link href="https://fonts.googleapis.com/css2?family=Lato:wght@300;400;700&display=swap" rel="stylesheet">
<style>
  :root {
    --stage: #2b2c2e;
    --card: #ffffff;
    --ink: #1d1d22;
    --ink-soft: #55565c;
    --navy: #0054aa;
    --blue: #0677ba;
    --sky-wash: #cadeef;
    --teal-wash: #c7ebf8;
    --pink-wash: #eddbeb;
    --lilac-wash: #e3daeb;
    --magenta: #a7469a;
    --plum: #6b429c;
    --teal: #00a99d;
  }
  * { box-sizing: border-box; margin: 0; padding: 0; }
  html, body { width: 1200px; height: 900px; overflow: hidden; }
  body {
    background: var(--stage);
    font-family: "Lato", sans-serif;
    display: flex;
    flex-direction: column;
    align-items: center;
    justify-content: center;
    gap: 40px;
  }
  .card {
    position: relative;
    width: 700px;
    height: 400px;
    background: var(--card);
    overflow: hidden;
    box-shadow: 0 10px 30px rgba(0,0,0,.45);
  }
  .card__wash {
    position: absolute;
    inset: 0;
    background:
      linear-gradient(180deg, rgba(255,255,255,0) 45%, rgba(202,222,239,.55) 100%),
      linear-gradient(90deg, rgba(199,235,248,.35) 0%, rgba(227,218,235,.35) 60%, rgba(237,219,235,.6) 100%);
  }
  .brand {
    position: absolute;
    font-weight: 300;
    color: var(--ink);
    text-align: right;
    line-height: 1;
  }
  .brand__main { display: block; font-size: 58px; letter-spacing: .5px; }
  .brand__sub { display: block; font-size: 26px; letter-spacing: 6px; margin-top: 4px; }
  .brand__dot {
    display: inline-block;
    width: 14px; height: 14px;
    border-radius: 50%;
    background: var(--plum);
    vertical-align: middle;
    margin-right: 12px;
    position: relative; top: -8px;
  }
  .card--front .brand { left: 130px; top: 150px; }
  .card--back .brand { left: 150px; top: 60px; }
  .card--back .brand__main { font-size: 46px; }
  .card--back .brand__sub { font-size: 21px; letter-spacing: 5px; }

  .holder {
    position: absolute;
    left: 0; right: 0;
    top: 180px;
    height: 40px;
  }
  .holder__rule {
    position: absolute;
    left: 30px; right: 30px; bottom: 6px;
    height: 2px;
    background: linear-gradient(90deg, var(--magenta) 0 55%, var(--plum) 55% 78%, var(--teal) 78% 100%);
  }
  .holder__name {
    position: absolute;
    left: 250px; bottom: 12px;
    font-weight: 700;
    font-size: 28px;
    color: var(--navy);
  }
  .holder__cred { font-size: 15px; margin-left: 6px; letter-spacing: .5px; }

  .contact {
    position: absolute;
    list-style: none;
    font-size: 19px;
    color: var(--ink-soft);
    line-height: 1.5;
  }
  .contact li { display: flex; align-items: center; gap: 10px; }
  .contact svg { width: 18px; height: 18px; fill: var(--blue); flex: none; }
  .contact--left { left: 40px; bottom: 40px; }
  .contact--right { right: 40px; bottom: 120px; text-align: right; }
  .contact--right li { justify-content: flex-end; }
</style>
</head>
<body>

<section class="card card--front" aria-label="Card front">
  <div class="card__wash"></div>
  <div class="brand">
    <span class="brand__main"><span class="brand__dot"></span>Quiet Harbor</span>
    <span class="brand__sub">Counseling</span>
  </div>
</section>

<section class="card card--back" aria-label="Card back">
  <div class="card__wash"></div>
  <div class="brand">
    <span class="brand__main"><span class="brand__dot"></span>Quiet Harbor</span>
    <span class="brand__sub">Counseling</span>
  </div>

  <div class="holder">
    <div class="holder__rule"></div>
    <p class="holder__name">Corra Mabbitt<span class="holder__cred">MS LMFT</span></p>
  </div>

  <ul class="contact contact--right">
    <li>www.quietharborcounsel.com
      <svg viewBox="0 0 24 24" aria-hidden="true"><path d="M12 2a10 10 0 1 0 0 20 10 10 0 0 0 0-20zm0 2c1 1.4 1.7 3.3 1.9 6h-3.8C10.3 7.3 11 5.4 12 4zm-2.6.5C8.7 6 8.2 7.9 8.1 10H4.3a8 8 0 0 1 5.1-5.5zm5.2 0A8 8 0 0 1 19.7 10h-3.8c-.1-2.1-.6-4-1.3-5.5zM4.3 12h3.8c.1 2.1.6 4 1.3 5.5A8 8 0 0 1 4.3 12zm5.8 0h3.8c-.2 2.7-.9 4.6-1.9 6-1-1.4-1.7-3.3-1.9-6zm5.8 0h3.8a8 8 0 0 1-5.1 5.5c.7-1.5 1.2-3.4 1.3-5.5z"/></svg>
    </li>
    <li>4175 Pemberly Suite 620
      <svg viewBox="0 0 24 24" aria-hidden="true"><path d="M12 2a7 7 0 0 0-7 7c0 5 7 13 7 13s7-8 7-13a7 7 0 0 0-7-7zm0 9.5a2.5 2.5 0 1 1 0-5 2.5 2.5 0 0 1 0 5z"/></svg>
    </li>
  </ul>

  <ul class="contact contact--left">
    <li>
      <svg viewBox="0 0 24 24" aria-hidden="true"><path d="M6.6 10.8a15 15 0 0 0 6.6 6.6l2.2-2.2a1 1 0 0 1 1-.25 11.4 11.4 0 0 0 3.6.57 1 1 0 0 1 1 1V20a1 1 0 0 1-1 1A17 17 0 0 1 3 4a1 1 0 0 1 1-1h3.5a1 1 0 0 1 1 1c0 1.25.2 2.45.57 3.57a1 1 0 0 1-.25 1z"/></svg>
      555-014-2286
    </li>
    <li>
      <svg viewBox="0 0 24 24" aria-hidden="true"><path d="M7 3h8l3 3v4H7zM4 10h16a2 2 0 0 1 2 2v6h-4v3H6v-3H2v-6a2 2 0 0 1 2-2zm4 6v3h8v-3z"/></svg>
      555-017-3390
    </li>
    <li>
      <svg viewBox="0 0 24 24" aria-hidden="true"><path d="M3 5h18a1 1 0 0 1 1 1v12a1 1 0 0 1-1 1H3a1 1 0 0 1-1-1V6a1 1 0 0 1 1-1zm1 2.4V17h16V7.4l-8 5.1z"/></svg>
      info@quietharborcounsel.com
    </li>
  </ul>
</section>

</body>
</html>
```